Redesign Website for Tandara Flame

I have an existing website on https://www.tandaraflame-example.com.au/ and would like to have this redesigned professionally with new content (please refer to word document). We are fire protection engineers providing fire services design expertise and engineering design to a range of different clients.

We also provide drafting services to clients in the form of completing final commissioning documentation such as 'as-installed' drawings and fire services block plans to ensure compliance with the building code and relevant Australian Standards.

Target Market(s)

Builders, Architects, Consultants, Project Managers

Industry/Entity Type

Engineering Consultant

Coding

Coded - Design and coding required

Number of Pages Required

4 page

Font styles to use
Sans Serif

Requirements
Must have
• Home and about Page, fire services design page, fire block plans page, contact us page (4 Pages).

The website colour choice must match or compliment the new company logo.
Nice to have
• Quality photos of fire services installations in buildings to Australian Standards.

A website similar to this would be ideal http://corbellpyro-example.com.au
Should not have
• Stolen licensed photos

```html
<!DOCTYPE html>
<html lang="en">
<head>
<meta charset="utf-8">
<title>Tandara Flame – Fire Services Drawings and Block Plans</title>
<link rel="stylesheet" href="https://fonts.googleapis.com/css2?family=Exo+2:ital,wght@0,300;0,400;0,500;0,600;0,700;0,800;1,400&display=swap">
<style>
:root{
  --orange:#f7941d;
  --orange-deep:#ef8a14;
  --ink:#111111;
  --text:#2b2b2b;
  --white:#ffffff;
  --grey-band:#efefef;
  --footer:#2a2525;
  --photo-dark:#3a3634;
  --photo-concrete:#a8a6a1;
}
*{box-sizing:border-box;margin:0;padding:0}
html,body{width:1200px;height:3668px;overflow:hidden}
body{font-family:"Exo 2",Arial,sans-serif;color:var(--text);background:var(--white);position:relative}
.abs{position:absolute}
a{color:inherit;text-decoration:none}

/* header */
.site-header{position:absolute;left:0;top:0;width:1200px;height:110px;background:var(--white)}
.brand{position:absolute;left:176px;top:38px;display:flex;align-items:center;gap:10px}
.brand-dot{width:26px;height:26px;border-radius:50%;background:var(--orange)}
.brand-name{font-weight:600;font-size:22px;color:var(--orange);letter-spacing:.5px}
.nav{position:absolute;top:0;left:0;font-size:12px;color:#333}
.nav a{position:absolute;top:46px;white-space:nowrap}
.nav .nav-home{left:566px;top:22px;width:52px;height:62px;display:flex;align-items:center;justify-content:center;color:var(--orange)}
.nav .nav-home svg{position:absolute;inset:0}
.nav .nav-home span{position:relative}
.social-top{position:absolute;left:1012px;top:47px;display:flex;gap:12px}
.social-top span{width:11px;height:11px;background:var(--orange);border-radius:2px}

/* hero */
.hero{position:absolute;left:0;top:110px;width:1200px;height:522px;
  background:linear-gradient(180deg,#4a4442 0%,#5a3b36 40%,#3b2f2d 100%)}
.hero::after{content:"";position:absolute;inset:0;background:rgba(20,18,18,.35)}
.hero-inner{position:absolute;inset:0;z-index:1;text-align:center;color:var(--white)}
.hero-title{position:absolute;left:0;width:100%;top:148px;font-size:86px;font-weight:700;letter-spacing:-1px;line-height:1}
.hero-sub{position:absolute;left:0;width:100%;top:248px;font-size:15px;letter-spacing:6.5px;font-weight:500}
.btn{display:flex;align-items:center;justify-content:center;font-size:11px;color:var(--white);background:var(--orange);border-radius:6px;text-transform:uppercase}
.hero .btn{position:absolute;left:535px;top:297px;width:128px;height:36px}
.marker{position:absolute;width:44px;height:44px;border-radius:50%;background:var(--white);border:4px solid var(--orange);z-index:3}

/* welcome */
.welcome-frame{position:absolute;left:128px;top:756px;width:417px;height:383px;background:var(--orange)}
.welcome-photo{position:absolute;left:141px;top:769px;width:417px;height:376px;
  background:linear-gradient(180deg,#b9b7b1 0%,#8d8b86 55%,#9f9a86 100%)}
.play{position:absolute;left:170px;top:160px;width:78px;height:54px;border-radius:12px;background:rgba(30,30,30,.75)}
.play::after{content:"";position:absolute;left:31px;top:15px;border-left:22px solid var(--white);border-top:12px solid transparent;border-bottom:12px solid transparent}
.welcome-kicker{position:absolute;left:605px;top:822px;font-size:29px;color:var(--ink);font-weight:400}
.welcome-title{position:absolute;left:605px;top:857px;font-size:45px;color:var(--ink);font-weight:700}
.welcome-text{position:absolute;left:605px;top:924px;width:420px;font-size:10.6px;line-height:24px;color:#222}
.welcome .btn{position:absolute;left:604px;top:1059px;width:122px;height:37px}

/* services */
.services{position:absolute;left:0;top:1251px;width:1200px;height:805px;
  background:linear-gradient(110deg,#f39a35 0%,#f7941d 45%,#f08e1c 100%)}
.section-title{position:absolute;left:0;width:100%;text-align:center;font-size:46px;font-weight:700}
.section-lede{position:absolute;text-align:center;font-size:11.3px;line-height:24px}
.services .section-title{top:74px;color:var(--white)}
.services .section-lede{left:220px;width:760px;top:142px;color:var(--white)}
.service-card{position:absolute;top:262px;width:289px;height:387px}
.service-label{position:absolute;left:8px;top:313px;width:265px;height:56px;background:var(--orange);color:var(--white);font-weight:700;font-size:16px;display:flex;align-items:center;padding-left:30px}
.btn-outline{position:absolute;left:540px;top:698px;width:122px;height:36px;border:1px solid var(--white);border-radius:6px;color:var(--white);font-size:11px;display:flex;align-items:center;justify-content:center}

/* block plans */
.blockplans .section-title{top:2146px;color:var(--ink)}
.blockplans .section-lede{left:200px;width:800px;top:2218px;color:#222}
.plan-card{position:absolute;top:2353px;width:289px;height:224px;border-radius:35px;background:var(--white);box-shadow:0 6px 18px rgba(0,0,0,.12);padding:0 28px;color:var(--ink)}
.plan-card.is-featured{background:var(--orange);color:var(--white)}
.plan-icon{position:absolute;left:28px;top:28px}
.plan-title{position:absolute;left:28px;top:78px;font-size:18px;font-weight:700;white-space:nowrap}
.plan-text{position:absolute;left:28px;top:113px;width:240px;font-size:10.8px;line-height:21px;height:42px;overflow:hidden}
.plan-arrow{position:absolute;left:28px;top:164px;width:34px;height:34px;border-radius:50%;background:var(--ink)}
.is-featured .plan-arrow{background:none;border:1.5px solid var(--white)}
.blockplans .btn{position:absolute;left:540px;top:2636px;width:122px;height:36px}

/* testimonials */
.testimonials{position:absolute;left:0;top:2743px;width:1200px;height:604px;background:var(--grey-band)}
.testimonials .section-title{top:94px;color:var(--ink)}
.quote-box{position:absolute;left:280px;top:263px;width:651px;height:215px;background:var(--white);box-shadow:0 8px 10px rgba(0,0,0,.05)}
.avatar{position:absolute;left:582px;top:228px;width:60px;height:60px;border-radius:50%;background:linear-gradient(135deg,#8a6652,#4a2f28);border:3px solid var(--white);z-index:2}
.quote-mark{position:absolute;font-size:54px;color:#bbb;font-style:italic;font-weight:700;line-height:1}
.quote-text{position:absolute;left:70px;top:58px;width:530px;text-align:center;font-size:11.3px;line-height:25px;font-style:italic;color:#333}
.quote-name{position:absolute;left:0;width:100%;top:176px;text-align:center;color:var(--orange);font-size:18px}
.slider-btn{position:absolute;top:353px;width:36px;height:36px;display:flex;align-items:center;justify-content:center}
.slider-prev{left:194px;background:#dcdcdc}
.slider-next{left:968px;background:var(--orange)}
.dots{position:absolute;left:584px;top:528px;display:flex;gap:4px;align-items:center}
.dots span{width:7px;height:7px;border-radius:50%;background:#bdbdbd}
.dots .on{width:9px;height:9px;background:var(--orange)}

/* footer */
.site-footer{position:absolute;left:0;top:3347px;width:1200px;height:321px;background:var(--footer);color:var(--white)}
.footer-brand{position:absolute;left:230px;top:78px;width:200px;text-align:center}
.footer-brand .brand-dot{margin:0 auto 14px;width:52px;height:52px;background:none;border:3px solid var(--white)}
.footer-brand .brand-name{color:var(--white);font-size:23px}
.footer-social{position:absolute;left:287px;top:186px;display:flex;gap:10px}
.footer-social span{width:23px;height:23px;border-radius:50%;background:var(--orange)}
.footer-heading{position:absolute;top:66px;font-size:19px;font-weight:700}
.footer-links{position:absolute;left:554px;top:119px;list-style:none;font-size:11px;line-height:22.7px}
.contact-list{position:absolute;left:813px;top:119px;list-style:none;font-size:11px}
.contact-list li{display:flex;align-items:center;gap:14px;height:31.5px}
.contact-list svg{width:14px;flex:none}
.footer-rule{position:absolute;left:0;top:269px;width:1200px;height:1px;background:#6b6464}
.copyright{position:absolute;left:0;width:100%;top:290px;text-align:center;font-size:11px}
</style>
</head>
<body>

<header class="site-header">
  <a class="brand" href="#"><span class="brand-dot"></span><span class="brand-name">TANDARA FLAME</span></a>
  <nav class="nav">
    <a class="nav-home" href="#"><svg width="52" height="62" viewBox="0 0 52 62"><polygon points="26,1 51,15.5 51,46.5 26,61 1,46.5 1,15.5" fill="none" stroke="#f7941d" stroke-width="1"/></svg><span>Home</span></a>
    <a href="#" style="left:640px">About Us</a>
    <a href="#" style="left:723px">Fire Services</a>
    <a href="#" style="left:822px">Fire Block Plans</a>
    <a href="#" style="left:937px">Contact Us</a>
  </nav>
  <div class="social-top" aria-label="Social links"><span></span><span></span><span></span></div>
</header>

<section class="hero" role="img" aria-label="Photo of a red fire pump and sprinkler valve room in a basement">
  <div class="hero-inner">
    <h1 class="hero-title">TANDARA FLAME</h1>
    <p class="hero-sub">FIRE SERVICES DRAWINGS AND BLOCK PLANS</p>
    <a class="btn" href="#">Our Services</a>
  </div>
</section>
<span class="marker" style="left:578px;top:618px"></span>

<section class="welcome">
  <div class="welcome-frame"></div>
  <div class="welcome-photo" role="img" aria-label="Video still of a basement car park entrance with yellow safety stripes"><span class="play"></span></div>
  <p class="welcome-kicker">Welcome To</p>
  <h2 class="welcome-title">Tandara Flame</h2>
  <p class="welcome-text">Tandara Flame is a company based in Sydney providing the Australian market expertise in the field of fire safety. Our mission is to assist builders, architects, fire contractors, consultants and project managers with the preparation of fire services design and specifications to meet regulatory requirements for Complying Development Certificate (CDC), Development Applications (DA) or Council Fire Orders.</p>
  <a class="btn" href="#">Read More</a>
</section>

<section class="services">
  <h2 class="section-title">Fire Services</h2>
  <p class="section-lede">We will assist and guide you throughout the fire services design process, whether you are installing a new fire safety system or upgrading an existing system, we will ensure your new or upgraded fire safety system will comply with applicable Fire Engineering Reports, the National Construction Code (NCC) and relevant Australian Standards and / or council, or other consent authority requirements.</p>
  <div class="service-card" style="left:141px;background:linear-gradient(180deg,#d8d6d2,#9c9890)" role="img" aria-label="Photo of a newly built corridor with exit sign">
    <span class="service-label">Smoke Alarms</span></div>
  <div class="service-card" style="left:455px;background:linear-gradient(180deg,#b5b3ae,#8a8884 70%,#a39b70)" role="img" aria-label="Photo of a basement car park with striped floor">
    <span class="service-label">Alarm Systems</span></div>
  <div class="service-card" style="left:769px;background:linear-gradient(180deg,#c22a25,#a41d1b 60%,#7e1a17)" role="img" aria-label="Photo of an open red fire hydrant booster cabinet">
    <span class="service-label">Occupant Warning Systems</span></div>
  <a class="btn-outline" href="#">READ MORE</a>
</section>
<span class="marker" style="left:578px;top:1231px"></span>
<span class="marker" style="left:578px;top:2034px"></span>

<section class="blockplans">
  <h2 class="section-title">Fire Block Plans</h2>
  <p class="section-lede">We can also assist our clients in the preparation commissioning documentation (i.e. zone block plan, fire hydrant block plans, sprinkler block plan) as required for relevant fire safety systems on completion of a project to achieve full compliance with relevant Australian Standards for project handover or for the update of existing outdated / missing block plans.</p>

  <article class="plan-card" style="left:141px">
    <svg class="plan-icon" width="50" height="36" viewBox="0 0 50 36"><ellipse cx="25" cy="9" rx="23" ry="7" fill="#111"/><rect x="6" y="14" width="38" height="8" rx="3" fill="#111"/><rect x="14" y="24" width="22" height="6" rx="2" fill="#111"/></svg>
    <h3 class="plan-title">Zone Block Plans</h3>
    <p class="plan-text">AS1670.1 requires an automatic smoke detection and alarm system to incorporate a</p>
    <span class="plan-arrow"><svg width="34" height="34" viewBox="0 0 34 34"><path d="M11 17h12M18 12l5 5-5 5" stroke="#fff" stroke-width="2" fill="none"/></svg></span>
  </article>

  <article class="plan-card is-featured" style="left:455px">
    <svg class="plan-icon" width="46" height="40" viewBox="0 0 46 40"><path d="M2 13h8l12-10v34L10 27H2z" fill="#fff"/><path d="M28 13c3 4 3 10 0 14M33 8c6 7 6 17 0 24" stroke="#fff" stroke-width="3" fill="none"/></svg>
    <h3 class="plan-title">EWIS / SSISEP Block Plans</h3>
    <p class="plan-text">AS1670.4 requires an Emergency Warning and Intercom System (EWIS) / Sound System and</p>
    <span class="plan-arrow"><svg width="31" height="31" viewBox="0 0 31 31"><path d="M9.5 15.5h12M16.5 10.5l5 5-5 5" stroke="#fff" stroke-width="2" fill="none"/></svg></span>
  </article>

  <article class="plan-card" style="left:769px">
    <svg class="plan-icon" width="46" height="40" viewBox="0 0 46 40"><rect x="17" y="2" width="12" height="12" fill="none" stroke="#111" stroke-width="2"/><path d="M23 14v8M23 22l-10 8M23 22l10 8M23 22v10M23 22l-17 5M23 22l17 5" stroke="#111" stroke-width="2"/><circle cx="6" cy="30" r="2" fill="#111"/><circle cx="13" cy="34" r="2" fill="#111"/><circle cx="23" cy="36" r="2" fill="#111"/><circle cx="33" cy="34" r="2" fill="#111"/><circle cx="40" cy="30" r="2" fill="#111"/></svg>
    <h3 class="plan-title">Sprinkler Block Plans</h3>
    <p class="plan-text">AS2118.1 requires Automatic Fire Sprinkler Systems to incorporate a Sprinkler Block Plan to</p>
    <span class="plan-arrow"><svg width="34" height="34" viewBox="0 0 34 34"><path d="M11 17h12M18 12l5 5-5 5" stroke="#fff" stroke-width="2" fill="none"/></svg></span>
  </article>

  <a class="btn" href="#">Read More</a>
</section>

<section class="testimonials">
  <h2 class="section-title">What Our Clients Say!</h2>
  <span class="avatar" role="img" aria-label="Client portrait"></span>
  <div class="quote-box">
    <span class="quote-mark" style="left:34px;top:32px">”</span>
    <p class="quote-text">Proin ut tempus erat, eget euismod lectus. Nullam aliquam faucibus turpis eget aliquet. Curabitur nec tortor dui. Pellentesque dignissim gravida urna in tristique. Nunc egestas tincidunt nulla in malesuada. Integer blandit porttitor nisl non lacinia. Praesent vehicula ac turpis non vehicula. Vivamus sed hendrerit leo. Nullam ultricies nunc turpis, id interdum libero placerat</p>
    <span class="quote-mark" style="left:526px;top:130px">“</span>
    <p class="quote-name">Name Here</p>
  </div>
  <a class="slider-btn slider-prev" href="#" aria-label="Previous"><svg width="18" height="14" viewBox="0 0 18 14"><path d="M17 7H2M7 1L1 7l6 6" stroke="#111" stroke-width="2" fill="none"/></svg></a>
  <a class="slider-btn slider-next" href="#" aria-label="Next"><svg width="18" height="14" viewBox="0 0 18 14"><path d="M1 7h15M11 1l6 6-6 6" stroke="#fff" stroke-width="2" fill="none"/></svg></a>
  <div class="dots"><span class="on"></span><span></span><span></span><span></span></div>
</section>

<footer class="site-footer">
  <div class="footer-brand"><div class="brand-dot"></div><span class="brand-name">TANDARA FLAME</span></div>
  <div class="footer-social" aria-label="Social links"><span></span><span></span><span></span></div>
  <h4 class="footer-heading" style="left:554px">Quick Links</h4>
  <ul class="footer-links">
    <li>Home</li><li>About Us</li><li>Fire Services</li><li>Fire Block Plans</li><li>Contact Us</li>
  </ul>
  <h4 class="footer-heading" style="left:813px">Let's Connect</h4>
  <ul class="contact-list">
    <li><svg viewBox="0 0 14 14"><path d="M7 1a4 4 0 0 1 4 4c0 3-4 8-4 8S3 8 3 5a4 4 0 0 1 4-4z" fill="#fff"/><circle cx="7" cy="5" r="1.5" fill="#2a2525"/></svg>123 lorem ipsum 456</li>
    <li><svg viewBox="0 0 14 14"><path d="M3 1l2.5 3-1.5 1.5c1 2 2.5 3.5 4.5 4.5L10 8.5l3 2.5-1.5 2C6 13 1 8 1 2.5z" fill="#fff"/></svg>+614 00 555 018</li>
    <li><svg viewBox="0 0 14 14"><rect x="1" y="3" width="12" height="8" fill="#fff"/><path d="M1 3l6 5 6-5" stroke="#2a2525" fill="none"/></svg>info@tandaraflame-example.com.au</li>
  </ul>
  <div class="footer-rule"></div>
  <p class="copyright">Copyright © 2021 Tandara Flame. All rights reserved.</p>
</footer>

</body>
</html>
```